Personal Injury Lawyer Billboard

I would like a design created featuring the image of the lawyer centered in the middle of the design.
To the left of the lawyer's image it should read "INJURED?"
To the right of the lawyer's image, it should read "CALL BRUNO!"
Under Call Bruno, include the phone number 318-555-0187.
At the bottom of the design include the lawyers information "Bruno Pemberly Accident & Injury Lawyers"
PLEASE REMOVED THE BACKGROUND IMAGERY OF THE PHOTO SUBMITTED. Also, the colors for this design should match the colors shown in the logo (navy, white and relective soft gold). Please use those color combinations in ways that best stand out.

```html
<!DOCTYPE html>
<html lang="en">
<head>
<meta charset="utf-8">
<title>Bruno Pemberly Accident &amp; Injury Lawyers – Billboard</title>
<link rel="stylesheet" href="https://fonts.googleapis.com/css2?family=Bebas+Neue&family=Oswald:wght@500&family=Merriweather:wght@900&display=swap">
<style>
  :root {
    --navy: #0e1a45;
    --navy-soft: #2f355a;
    --gold-light: #e2c24d;
    --gold: #e59d22;
    --gold-pale: #d9d47e;
    --white: #ffffff;
    --stage: #e4e4e6;
    --photo-top: #3a4470;
    --photo-bottom: #16204d;
  }
  * { margin: 0; padding: 0; box-sizing: border-box; }
  html, body {
    width: 1091px;
    height: 1200px;
    overflow: hidden;
    background: var(--stage);
  }
  .billboard {
    position: absolute;
    left: 30px;
    top: 430px;
    width: 1031px;
    height: 340px;
    box-shadow: 0 14px 28px rgba(0,0,0,0.35);
  }
  .billboard svg { display: block; width: 100%; height: 100%; }
  .headline { font-family: "Bebas Neue", "Oswald", sans-serif; }
  .firm-name { font-family: "Oswald", "Bebas Neue", sans-serif; font-weight: 500; }
  .web-address { font-family: "Oswald", sans-serif; font-weight: 500; }
  .footer-name { font-family: "Merriweather", Georgia, serif; font-weight: 900; }
</style>
</head>
<body>
<div class="billboard">
  <svg viewBox="0 0 1031 340" xmlns="http://www.w3.org/2000/svg">
    <defs>
      <linearGradient id="goldPanel" x1="0" y1="0" x2="1" y2="0">
        <stop offset="0" stop-color="var(--gold)"/>
        <stop offset="1" stop-color="var(--gold-light)"/>
      </linearGradient>
      <linearGradient id="goldType" x1="0" y1="0" x2="0" y2="1">
        <stop offset="0" stop-color="var(--gold-pale)"/>
        <stop offset="1" stop-color="var(--gold)"/>
      </linearGradient>
      <linearGradient id="goldRule" x1="0" y1="0" x2="1" y2="0">
        <stop offset="0" stop-color="var(--gold)"/>
        <stop offset="1" stop-color="var(--gold-pale)"/>
      </linearGradient>
      <linearGradient id="photoTone" x1="0" y1="0" x2="0" y2="1">
        <stop offset="0" stop-color="var(--photo-top)"/>
        <stop offset="1" stop-color="var(--photo-bottom)"/>
      </linearGradient>
    </defs>

    <!-- main navy field -->
    <rect class="field-navy" x="0" y="0" width="1031" height="271" fill="var(--navy)"/>
    <!-- diagonal accent band -->
    <polygon class="accent-band" points="274,0 490,0 620,271 430,271" fill="var(--navy-soft)"/>
    <!-- gold call panel -->
    <polygon class="call-panel" points="490,0 1031,0 1031,221 635,221" fill="url(#goldPanel)"/>
    <!-- web address strip -->
    <rect class="web-strip" x="635" y="221" width="396" height="50" fill="var(--navy)"/>
    <!-- footer band -->
    <rect class="footer-band" x="0" y="271" width="1031" height="69" fill="var(--white)"/>

    <!-- headline left -->
    <text class="headline" x="31" y="150" font-size="148" fill="var(--navy-soft)" textLength="392" lengthAdjust="spacingAndGlyphs">INJURED?</text>
    <text class="headline" x="27" y="146" font-size="148" fill="url(#goldType)" textLength="392" lengthAdjust="spacingAndGlyphs">INJURED?</text>

    <!-- firm name -->
    <text class="firm-name" x="43" y="212" font-size="44" fill="var(--white)" textLength="256" lengthAdjust="spacingAndGlyphs">BRUNO PEMBERLY</text>
    <line class="firm-rule" x1="43" y1="222" x2="299" y2="222" stroke="url(#goldRule)" stroke-width="1.5"/>
    <text class="firm-name" x="43" y="249" font-size="24" fill="var(--white)" textLength="256" lengthAdjust="spacingAndGlyphs">ACCIDENT &amp; INJURY LAWYERS</text>
    <line class="firm-rule" x1="43" y1="257" x2="299" y2="257" stroke="url(#goldRule)" stroke-width="1.5"/>

    <!-- lawyer portrait -->
    <rect class="lawyer-portrait" x="438" y="16" width="192" height="255" rx="6" fill="url(#photoTone)" role="img" aria-label="Portrait of the lawyer in a navy suit and green tie, smiling with a raised fist"/>

    <!-- call to action -->
    <text class="headline" x="646" y="116" font-size="104" fill="var(--white)" textLength="350" lengthAdjust="spacingAndGlyphs">CALL BRUNO!</text>
    <text class="headline" x="646" y="192" font-size="80" fill="var(--navy)" textLength="350" lengthAdjust="spacingAndGlyphs">318-555-0187</text>

    <!-- web address -->
    <text class="web-address" x="676" y="258" font-size="28" fill="var(--white)" textLength="320" lengthAdjust="spacingAndGlyphs">WWW.BRUNOPEMBERLY.COM</text>

    <!-- footer firm name -->
    <text class="footer-name" x="45" y="317" font-size="26" fill="var(--navy)" textLength="945" lengthAdjust="spacingAndGlyphs">BRUNO PEMBERLY ACCIDENT &amp; INJURY LAWYERS</text>
  </svg>
</div>
</body>
</html>
```